Flyer Design

Meadowbright Cleaning Service LTD its all about cleaning ( Domestic Cleaning, Commercial Cleaning, Student Accommodations, Corridors, Halls & Common Areas). I'm looking for POSH/ ELEGANT LOOKING design of flyers, which presents all Services we provide, it also should include 5% discount for new customers, contact details: website: www.meadowbright-clean.co.uk email address: meadowbrightservice@mailnest.co.uk Mobile phone no: 07812036471 and home no: 01632960418 . I would like to include logo of the company, without any pictures of buckets etc.(that in my opinion pictures like that looks "cheap"). It should be design which perfectly match logo of the company, I would like also to include slogan of Meadowbright "You Deserve Meadowbright Cleaners". I was thinking to make those flyers, bright "clean" (maybe background could be beige color, on the other hand I think Navy color looks elegant as well, I'm looking for something posh NOT like some random cleaning company, It should be something UNIQUE). Of course by this flyers Meadowbright Cleaning Service should increase profits. If you will have any draft or any questions please contact me at any time on email: i.wrzesniak@mailnest.co.uk or by phone: 07812036471
Best Regards
Ilona Wrzesniak
Meadowbright Cleaning Service LTD

```html
<!DOCTYPE html>
<html lang="en">
<head>
<meta charset="utf-8">
<title>Meadowbright Cleaning Service – Flyer</title>
<link rel="stylesheet" href="https://fonts.googleapis.com/css2?family=Tinos:ital,wght@0,400;0,700;1,400;1,700&display=swap">
<style>
  :root {
    --navy: #1f2170;
    --paper: #fbfaf6;
    --beige: #efe5cc;
    --beige-soft: #f5efdf;
    --swoosh: rgba(255, 255, 255, 0.85);
    --ornament-a: #9fd4e3;
    --ornament-b: #5fb3c9;
  }
  * { margin: 0; padding: 0; box-sizing: border-box; }
  html, body { width: 1200px; height: 850px; overflow: hidden; background: #ffffff; }
  .flyer {
    position: relative;
    width: 1200px;
    height: 850px;
    overflow: hidden;
    background:
      radial-gradient(ellipse 70% 40% at 60% 30%, #ffffff 0%, rgba(255,255,255,0) 70%),
      linear-gradient(180deg, var(--paper) 0%, var(--beige-soft) 45%, var(--beige) 70%, var(--beige-soft) 100%);
    font-family: "Tinos", "Times New Roman", serif;
    color: var(--navy);
  }
  .flyer__swooshes { position: absolute; inset: 0; }
  .flyer__ornament { position: absolute; }
  .flyer__ornament--top-right { left: 800px; top: 10px; width: 400px; height: 395px; }
  .flyer__ornament--bottom-left { left: 18px; top: 445px; width: 380px; height: 390px; }

  .flyer__text { position: absolute; white-space: nowrap; line-height: 1; font-style: italic; }
  .headline { left: 128px; top: 115px; font-size: 46px; font-weight: 700; letter-spacing: 5.2px; }
  .pitch { left: 152px; top: 225px; font-size: 25px; font-weight: 400; letter-spacing: 3.6px; line-height: 50px; }
  .pitch span { display: block; height: 50px; }
  .slogan { left: 400px; top: 505px; font-size: 34px; font-weight: 700; letter-spacing: 4px; }
  .contact { left: 143px; top: 551px; font-size: 19px; font-weight: 700; letter-spacing: 3px; }
  .contact__label { display: block; margin-left: 9px; height: 44px; }
  .contact__line { display: block; height: 42.5px; }

  .brand {
    position: absolute;
    left: 880px;
    top: 722px;
    width: 240px;
    text-align: center;
    font-family: "Tinos", "Times New Roman", serif;
    font-weight: 400;
    font-style: normal;
    color: var(--navy);
    line-height: 1.15;
  }
  .brand__name { display: block; font-size: 27px; }
  .brand__sub { display: block; font-size: 17px; }
</style>
</head>
<body>
<main class="flyer">
  <svg class="flyer__swooshes" width="1200" height="850" viewBox="0 0 1200 850" aria-hidden="true">
    <g fill="none" stroke="var(--swoosh)" stroke-linecap="round">
      <path d="M-20 120 C 300 60, 600 240, 1220 150" stroke-width="3"/>
      <path d="M-20 300 C 250 200, 700 420, 1220 260" stroke-width="2"/>
      <path d="M-20 420 C 400 330, 800 520, 1220 380" stroke-width="4"/>
      <path d="M-20 560 C 350 470, 750 650, 1220 500" stroke-width="2"/>
      <path d="M-20 700 C 300 640, 800 760, 1220 640" stroke-width="3"/>
      <path d="M200 850 C 500 740, 850 780, 1220 720" stroke-width="2"/>
    </g>
  </svg>

  <svg class="flyer__ornament flyer__ornament--top-right" viewBox="0 0 400 395" role="img" aria-label="Ornamental teal scrollwork framing the top-right corner">
    <defs>
      <linearGradient id="ornament-fade-tr" x1="0" y1="0" x2="1" y2="1">
        <stop offset="0" stop-color="var(--ornament-a)" stop-opacity="0.55"/>
        <stop offset="1" stop-color="var(--ornament-b)" stop-opacity="0.55"/>
      </linearGradient>
    </defs>
    <path d="M0 15 H390 V395 H320 V90 H0 Z" fill="url(#ornament-fade-tr)"/>
  </svg>

  <svg class="flyer__ornament flyer__ornament--bottom-left" viewBox="0 0 380 390" role="img" aria-label="Ornamental teal scrollwork framing the bottom-left corner">
    <defs>
      <linearGradient id="ornament-fade-bl" x1="0" y1="0" x2="1" y2="1">
        <stop offset="0" stop-color="var(--ornament-a)" stop-opacity="0.55"/>
        <stop offset="1" stop-color="var(--ornament-b)" stop-opacity="0.55"/>
      </linearGradient>
    </defs>
    <path d="M10 0 H75 V310 H380 V385 H10 Z" fill="url(#ornament-fade-bl)"/>
  </svg>

  <h1 class="flyer__text headline">5% discount for new customers</h1>

  <p class="flyer__text pitch">
    <span>Require help for cleaning?</span>
    <span>Meadowbright Cleaning Service is what you need</span>
    <span>From Domestic Cleaning</span>
    <span>To Commercial Cleaning</span>
    <span>its all about cleaning</span>
  </p>

  <p class="flyer__text slogan">You Deserve Meadowbright Cleaners</p>

  <address class="flyer__text contact">
    <span class="contact__label">contact details:</span>
    <span class="contact__line">website: www.meadowbright-clean.co.uk</span>
    <span class="contact__line">email address: meadowbrightservice@mailnest.co.uk</span>
    <span class="contact__line">Mobile phone no: 07812036471</span>
    <span class="contact__line">home no: 01632960418</span>
  </address>

  <div class="brand">
    <span class="brand__name">Meadowbright</span>
    <span class="brand__sub">Cleaning Service LTD</span>
  </div>
</main>
</body>
</html>
```